Wheels and Haulers OnOffer Price Sheet

Front and back marketing / Price Sheet hand-out. 5.5 x 8.5 Attached find images you can use and basic text data. We are looking for an innovated designer that can take this data and create an appealing hand-out that will be presented to car dealerships.
The related website is www.wheelsandhaulers.onoffer
Sleek, aggressive, impressive, appealing to an age range of 30+. Professional clientele suits.
We list car ads on our VELNO TV network and on our website. Our customers are national car / truck dealerships and individuals who want to sell a vehicle. This hand-out should advertise our company, our services and give them a look at our basic pricing.
Updates

We were so super pleased with the very first design that we boosted our budget up by 25%! You guys have talent!

Project Deadline Extended
Reason: we posted this over a USA holiday and think we can get more designs if we extend

Target Market(s)

Car and Truck Dealers across the USA

Industry/Entity Type

Marketing

Font styles to use
Serif
Sans Serif

Requirements
Must have
• Clarity in defining the price plans. The wire frame of the cars and the for sale sign as seen in the provided image.

```html
<!DOCTYPE html>
<html lang="en">
<head>
<meta charset="utf-8">
<title>Wheels and Haulers OnOffer – Price Sheet</title>
<link rel="stylesheet" href="https://fonts.googleapis.com/css2?family=Josefin+Sans:wght@300;400;600&family=Playfair+Display:wght@400;700;900&family=Roboto+Condensed:wght@400;700&display=swap">
<style>
  :root {
    --bg-dark: #1c1c1d;
    --bg-mid: #3a3a3c;
    --purple: #5c2c86;
    --purple-deep: #47206a;
    --white: #ffffff;
    --panel-grey: #c8c8ca;
    --rule-grey: #a9a9ad;
    --ink: #2a2a2a;
    --sign-red: #d42a2a;
    --footer-text: #d9d9d9;
  }
  * { box-sizing: border-box; margin: 0; padding: 0; }
  html, body { width: 784px; height: 1200px; overflow: hidden; background: var(--bg-dark); }
  .sheet {
    position: relative;
    width: 784px; height: 1200px;
    overflow: hidden;
    background: radial-gradient(ellipse at 50% 45%, var(--bg-mid) 0%, #2a2a2c 55%, var(--bg-dark) 100%);
    font-family: "Roboto Condensed", Arial, sans-serif;
    color: var(--ink);
  }
  .vehicle-art {
    position: absolute; top: 8px;
    width: 170px; height: 88px;
    border-radius: 10px;
    background: linear-gradient(160deg, rgba(255,255,255,0.18), rgba(255,255,255,0.05));
  }
  .vehicle-art.truck { left: 4px; }
  .vehicle-art.car { right: 4px; }
  .brand {
    position: absolute; top: 14px; left: 0; right: 0;
    display: flex; justify-content: center; align-items: center; gap: 22px;
  }
  .brand-name {
    font-family: "Playfair Display", Georgia, serif;
    font-weight: 400; font-size: 44px; color: var(--white); letter-spacing: 1px;
  }
  .brand-square { width: 64px; height: 64px; background: var(--sign-red); border: 3px solid var(--white); }
  .plan {
    position: absolute; left: 118px; width: 548px;
    border: 4px solid var(--white); border-radius: 14px;
    background: var(--panel-grey); overflow: hidden;
    box-shadow: 0 6px 18px rgba(0,0,0,0.55);
  }
  .purple-band { background: var(--purple); padding-bottom: 8px; }
  .plan-title {
    color: var(--white);
    font-family: "Josefin Sans", Arial, sans-serif;
    font-weight: 300; font-size: 40px; line-height: 1;
    padding: 10px 18px 6px;
  }
  .plan-price {
    display: flex; align-items: flex-start; gap: 12px;
    margin: 0 10px; padding: 6px 12px;
    background: var(--white);
    border: 3px solid var(--purple-deep);
    border-radius: 6px;
  }
  .price {
    font-family: "Playfair Display", Georgia, serif;
    font-weight: 900; font-size: 50px; line-height: 1.1; color: var(--purple);
    padding-right: 12px; border-right: 3px solid var(--purple);
  }
  .price-terms {
    font-family: "Playfair Display", Georgia, serif; font-weight: 700;
    color: var(--purple); font-size: 15px; line-height: 1.2; padding-top: 3px;
  }
  .price-terms .network { font-size: 17px; color: var(--ink); }
  .plan-details { list-style: none; padding: 4px 10px 6px; }
  .plan-details li {
    font-weight: 700; font-size: 15px; line-height: 18px; color: var(--ink);
    padding: 6px 8px 5px; border-bottom: 1px solid var(--rule-grey);
  }
  .plan-details li:last-child { border-bottom: none; }
  .plan.special { top: 118px; }
  .plan.dealer { top: 431px; }
  .plan.bonus { top: 740px; }
  .footer { position: absolute; left: 0; right: 0; top: 1090px; text-align: center; color: var(--footer-text); }
  .footer .note-lead { font-family: "Josefin Sans", Arial, sans-serif; font-size: 18px; line-height: 22px; }
  .footer .note { font-family: "Josefin Sans", Arial, sans-serif; font-size: 12px; line-height: 16px; margin-top: 2px; }
  .footer .contact { font-family: "Josefin Sans", Arial, sans-serif; font-size: 30px; line-height: 36px; margin-top: 6px; letter-spacing: 0.5px; color: var(--white); }
</style>
</head>
<body>
<main class="sheet">
  <div class="vehicle-art truck" role="img" aria-label="White wireframe drawing of a pickup truck"></div>
  <div class="vehicle-art car" role="img" aria-label="White wireframe drawing of a sports car"></div>
  <header class="brand">
    <span class="brand-name">Wheels &amp; Haulers</span>
    <span class="brand-square"></span>
  </header>

  <section class="plan special">
    <div class="purple-band">
      <h2 class="plan-title">Special Deal</h2>
      <div class="plan-price">
        <span class="price">$30</span>
        <div class="price-terms"><div class="network">VELNO TV</div>$1 a day / 1 ad for 30 days minumum</div>
      </div>
    </div>
    <ul class="plan-details">
      <li>Max cars: 1</li>
      <li>Disk Storage: 30 MB</li>
      <li>Featured Cars: 0</li>
      <li>Account Life Time: 30 days</li>
    </ul>
  </section>

  <section class="plan dealer">
    <div class="purple-band">
      <h2 class="plan-title">Dealer Package</h2>
      <div class="plan-price">
        <span class="price">$810</span>
        <div class="price-terms"><div class="network">VELNO TV</div>90¢ a day / 10 ad for 90 days minumum</div>
      </div>
    </div>
    <ul class="plan-details">
      <li>Max cars: 10</li>
      <li>Disk Storage: 200 MB</li>
      <li>Featured Cars: 0</li>
      <li>Account Life Time: 90 days</li>
    </ul>
  </section>

  <section class="plan bonus">
    <div class="purple-band">
      <h2 class="plan-title">Bonus Dealer Package</h2>
      <div class="plan-price">
        <span class="price">$810</span>
        <div class="price-terms"><div class="network">VELNO TV</div>90¢ a day / 10 ad for 90 days minumum<br>PLUS 3 featured vehicles on both<br>VELNO TV and the WEB</div>
      </div>
    </div>
    <ul class="plan-details">
      <li>Max cars: 10</li>
      <li>Disk Storage: 200 MB</li>
      <li>Featured Cars: 3</li>
      <li>Account Life Time: 90 days</li>
    </ul>
  </section>

  <footer class="footer">
    <p class="note-lead">Featured packages may be bought as add-ons.</p>
    <p class="note">If you want a larger package please call us we offer an execute package for the elite client.</p>
    <p class="contact">WheelsandHaulers.OnOffer&nbsp; 817-555-0148</p>
  </footer>
</main>
</body>
</html>
```